Ansprechendes Layout für Geschichte von Oldtimern
Grossartiges Design, supernette Zusammenarbeit, megaschnelle Rückmeldung auf meine dusseligen Fragen - dass "Kastrel Ubo" sich meines Projektes angenommen hat, war ein echter Glückstreffer! Ich bin sowohl mit dem Ergebnis als auch mit der Kommunikation während des gesamten Prozesses absolut happy! Das hat richtig Spaß gemacht und auf meine Oldtimer-"Broschüre" bin ich stolz wie Bolle... Schade, dass man hier nicht 10 Sterne vergeben kann - "Kastrel Ubo" hätte sie verdient!
Zielgruppe
Ich mache mich aktuell selbstständig als Solo-Freiberuflerin (Redakteurin) mit dem Projekt 'Die Lack-Ballade': Ich schreibe für Oldtimer-Besitzer die Lebensgeschichte ihres Oldtimers auf - lebendig und augenzwinkernd. Zielgruppe: Oldtimer-Besitzer, die die Historie ihres Wagens als individuelles 'Buch' haben möchten; für sich selbst oder auch als Verkaufsargument beim Weiterverkauf des Oldtimers.
Aufgabenstellung
Mein Text wird auf hochwertigem Papier (einseitig) gedruckt , im Format A4 quer. Ein paar gut platzierte Fotos sollen den Text 'auflockern'. Für dieses Layout von Titelseite sowie Text & Fotos suche ein 'hinreißendes' Design (Schriften und Layout). Die fertigen Seiten werden dann in einer Druckerei ausgedruckt und in einen A4 Querformat-Klemmbinder 'reingesteckt'. Deswegen muss links entsprechend viel Rand/Platz gelassen werden. Wichtig ist mir eine sehr edle und hochwertige Anmutung des Layouts. Es soll kein 'Bildband' werden, die Fotos ergänzen lediglich den Text, der 'im Mittelpunkt' steht.

```html
<!DOCTYPE html>
<html lang="de">
<head>
<meta charset="utf-8">
<title>Die Lack-Ballade – Seiten</title>
<link rel="stylesheet" href="https://fonts.googleapis.com/css2?family=Carlito:wght@400&display=swap">
<style>
  :root {
    --gold: #b7a15c;
    --charcoal: #333333;
    --paper: #ffffff;
    --ink: #1a1a1a;
    --backdrop: #ffffff;
  }
  * { margin: 0; padding: 0; box-sizing: border-box; }
  html, body {
    width: 1200px; height: 2554px; overflow: hidden;
    background: var(--backdrop);
  }
  .canvas { position: relative; width: 1200px; height: 2554px; }
  .page {
    position: absolute; left: 45px; width: 1112px; height: 787px;
    background: var(--paper);
    box-shadow: 3px 4px 6px rgba(0,0,0,0.35);
  }
  .page--one { top: 65px; }
  .page--two { top: 895px; }
  .page--three { top: 1718px; }
  .page__topbar { position: absolute; left: 0; top: 0; width: 100%; height: 13px; background: var(--charcoal); }
  .page__footbar { position: absolute; left: 0; bottom: 0; width: 100%; height: 30px; background: var(--gold); }

  .brand {
    position: absolute; right: 77px; top: 62px;
    display: flex; flex-direction: column; align-items: flex-end;
  }
  .brand__row { display: flex; align-items: center; gap: 12px; }
  .brand__square { width: 34px; height: 34px; background: var(--gold); }
  .brand__name {
    font-family: "Carlito", "Calibri", sans-serif; font-weight: 400;
    font-size: 38px; line-height: 44px; color: var(--gold);
  }
  .brand__tagline {
    margin-top: 10px;
    font-family: "Carlito", "Calibri", sans-serif; font-size: 14px; letter-spacing: 0.6px;
    color: var(--gold); text-transform: uppercase;
  }

  .photo { position: absolute; }
  .photo--side { left: 118px; top: 337px; width: 347px; height: 230px;
    background: linear-gradient(180deg, #3f6a2c 0%, #2f4d24 40%, #1f2533 55%, #1c2230 78%, #9a8c88 80%, #b3a6a2 100%); }
  .photo--front { left: 119px; top: 309px; width: 466px; height: 287px;
    background: linear-gradient(180deg, #2c4a1e 0%, #3c5e2a 30%, #1e2535 48%, #1a2030 80%, #c9c6c0 84%, #dcdad6 100%); }

  .copy {
    position: absolute;
    font-family: "Carlito", "Calibri", sans-serif;
    font-size: 15.6px; line-height: 19.8px; color: var(--ink);
    text-align: justify; hyphens: manual;
  }
  .copy--intro { left: 504px; top: 333px; width: 529px; }
  .copy--left { left: 118px; top: 315px; width: 427px; }
  .copy--right { left: 606px; top: 315px; width: 427px; }
  .copy--closing { left: 623px; top: 306px; width: 410px; }
</style>
</head>
<body>
<div class="canvas">

  <section class="page page--one">
    <div class="page__topbar"></div>
    <div class="brand">
      <div class="brand__row"><span class="brand__square"></span><span class="brand__name">Die Lack-Ballade</span></div>
      <p class="brand__tagline">Lebensgeschichten klassischer Automobile</p>
    </div>
    <div class="photo photo--side" role="img" aria-label="Foto: dunkelblaue Oldtimer-Limousine in Seitenansicht vor einer grünen Hecke"></div>
    <p class="copy copy--intro">Lass mich mal eben nachrechnen: Wie alt war ich eigentlich damals, 1993? Ja, jetzt hab‘ ich’s: 26! Grandioses Auto-Alter, wenn Du mich fragst. Man ist erfahren, gelassen, souverän. Wissbegierig und neugierig war ich sowieso schon immer: Interessiert habe ich stets die Ohren gespitzt, wenn meine Fahrgäste über die aktuelle Politik oder die allgemeine Wirtschaftslage diskutiert haben. 1993 beherrschte gerade der Vertrag von Maastricht, mit dem die Europäische Union erstmals Wirklichkeit wurde, die Berichterstattung in allen Gazetten. Das bot natürlich reichlich Zündstoff für Diskussionen. Da ging es manchmal ganz schön hoch her, wenn Fahrer und Beifahrer über das Pro und Contra philosophierten… Ach, und dann war doch damals im Januar auch noch der Amtsantritt des neuen amerikanischen Präsidenten Walter Brenner. Das war doch der, der später dann mit seiner Frisur…? Na, Du weißt schon…</p>
    <div class="page__footbar"></div>
  </section>

  <section class="page page--two">
    <div class="page__topbar"></div>
    <div class="brand">
      <div class="brand__row"><span class="brand__square"></span><span class="brand__name">Die Lack-Ballade</span></div>
      <p class="brand__tagline">Lebensgeschichten klassischer Automobile</p>
    </div>
    <p class="copy copy--left">Nur um das an dieser Stelle gleich mal klarzustellen: Ich war natürlich niemals ein schnödes Taxi. Nix da mit Fahrten für Jedermann! Ich war in meinem ersten Leben ein ganz besonderer Dienstwagen – nämlich der Direktionswagen vom Nähmaschinen-Handel Kornhaupt! Mit piekfeiner Firmenadresse, wie sich das gehört: Hamburg, Lindenhofstraße 1. Jawohl! Mit standesgemäßer Sonderausstattung: elegantes Elfenbein-Lenkrad! Kuschelige Schlummerrolle für die Frau auf der Beifahrerseite! Hochwertiges Kessler-Bolero-Radio! Stolze 95 PS! Und natürlich das gesamte Sicherheitspaket. 8.665 Mark musste Nähmaschinen Kornhaupt 1967, als ich unter der Bezeichnung Typ K2/200 als elegante Viertürer-Limousine gebaut wurde, auf den Tisch legen. Kennst Du dieses Unternehmen eigentlich heutzutage noch? Das war ja eine ganz große Nummer damals! Gegründet wurde Nähmaschinen Kornhaupt 1871 von einem gewissen Anton Kornhaupt.</p>
    <p class="copy copy--right">Der war eigentlich gelernter Uhrmacher, sattelte dann aber um und baute sein Unternehmen zu einem der Marktführer in Sachen Nähmaschinen auf. Gleichzeitig lag ihm viel an seinen Leuten: Er richtete eine Werkskantine ein und kurz darauf auch eine eigene Betriebsbücherei. Schon bald lieferte die Firma ihre Nähmaschinen in viele Länder; 1938 wurde bereits die zweimillionste Maschine gefertigt. Und ausgerechnet in dem Jahr, in dem ich vom Band lief, brachte das Unternehmen eine ganz neue Overlock-Maschine heraus – mit 5.000 Stichen pro Minute! Goldene Zeiten waren das für Kornhaupt, auch für mich in Hamburg. Leider ist von dem damaligen Glanz und der einstigen Größe nicht mehr viel übriggeblieben: Heute gehört das Unternehmen einem fernen Konzern. Aber wir wollen ja jetzt nicht sentimental werden…</p>
    <div class="page__footbar"></div>
  </section>

  <section class="page page--three">
    <div class="page__topbar"></div>
    <div class="brand">
      <div class="brand__row"><span class="brand__square"></span><span class="brand__name">Die Lack-Ballade</span></div>
      <p class="brand__tagline">Lebensgeschichten klassischer Automobile</p>
    </div>
    <div class="photo photo--front" role="img" aria-label="Foto: dunkelblaue Oldtimer-Limousine schräg von vorn mit Weißwandreifen vor Bäumen"></div>
    <p class="copy copy--closing">Wusstest Du übrigens, dass in meinem Geburtsjahr 1967 das Benzin gerade mal 59 Pfennige und Diesel 56 Pfennige pro Liter kostete? Nur mal, so zum Vergleich: Heute, im Jahr 2021, zahlt man an der Tankstelle für einen Liter Super knapp 1,50 Euro, und für den Liter Diesel knapp 1,30 Euro! Rechne diese Preissteigerung jetzt bloß nicht noch in DM um… Ach, es waren einfach ganz andere Zeiten damals: Unser Bundeskanzler hieß Konrad Albers, Eintracht Wesertal wurde Deutscher Fußballmeister, die jungen Damen trugen bevorzugt verwegen kurze Miniröcke, und wenn man mein Radio anschaltete, gab’s tolle Musik von den Nightbirds, den Silver Pebbles oder auch von Reinhold Lenz, der damals gerade sein erstes Album veröffentlichte. Ganz schön lange her das alles, aber ich erinnere mich daran, als ob es erst gestern gewesen wäre… Aber ich schweife wohl etwas ab…</p>
    <div class="page__footbar"></div>
  </section>

</div>
</body>
</html>
```